White Cane Law Awareness Poster

Bright Harbor is a disability advocacy organization in Indiana. We are working on a project with the Cedarbrook Society of Staff for Low Sight. Our organizations need a design for a poster to promote awareness of Indiana's White Cane law. This poster will be displayed in local libraries, businesses, and other public places.

The poster should catch people's attention, and briefly explain that drivers have to yield for pedestrians who are blind who have white canes or seeing eye dogs.

The poster should be designed with people with low vision in mind. This means large text in a clear font, with good contrast between the text and the background. The text should be in a sans serif font that is clear and easy to read, with no italics or script fonts. There should not be a "busy" picture or pattern behind the text.

The poster should also include a reference to the relevant laws. We have attached a document with those references.

Finally, the poster should include the logos of Bright Harbor and the Cedarbrook Society of Staff for Low Sight, which we have included as attachments.

We have also included an attachment with a photo of the old White Cane Law poster, just to show an example of what we DO NOT want.

Industry/Entity Type

Non-Profit

Font styles to use
Sans Serif

Requirements
Must have
• The poster should also include a reference to the relevant laws. We have attached a document with those references.
• Finally, the poster should include the logos of Bright Harbor and the Cedarbrook Society of Staff for Low Sight, which we have included as attachments.

```html
<!DOCTYPE html>
<html lang="en">
<head>
<meta charset="utf-8">
<title>White Cane Law Awareness Poster</title>
<link rel="stylesheet" href="https://fonts.googleapis.com/css2?family=Oswald:wght@600;700&family=Arimo:wght@400;700&display=swap">
<style>
  :root {
    --red: #c8141b;
    --red-deep: #6e0508;
    --red-shadow: #8f0b10;
    --ink: #1b1819;
    --white: #ffffff;
    --grey: #6a6a6a;
    --navy: #1c2d6b;
  }
  * { margin: 0; padding: 0; box-sizing: border-box; }
  html, body { width: 857px; height: 1200px; overflow: hidden; background: var(--white); }
  .poster { position: relative; width: 857px; height: 1200px; overflow: hidden; font-family: "Arimo", Arial, sans-serif; }

  .hero {
    position: absolute; left: 0; top: 0; width: 857px; height: 680px;
    background: radial-gradient(ellipse 75% 70% at 42% 45%, var(--red) 0%, #a90f15 50%, var(--red-deep) 100%);
  }
  .figure-area {
    position: absolute; left: 585px; top: 50px; width: 250px; height: 620px;
    background: linear-gradient(180deg, var(--red-shadow), #7a080c);
    border-radius: 110px 110px 0 0;
    opacity: 0.85;
  }
  .stop-sign { position: absolute; left: 363px; top: 22px; }
  .headline {
    position: absolute; left: 52px; top: 250px;
    font-family: "Oswald", "Arial Narrow", sans-serif; font-weight: 700;
    color: var(--white); text-transform: uppercase; line-height: 0.95;
  }
  .headline .line { display: block; font-size: 150px; letter-spacing: 1px; }
  .headline .state-law { display: block; font-size: 112px; text-transform: none; margin-top: 6px; font-weight: 600; }

  .law-band {
    position: absolute; left: 0; top: 680px; width: 857px; height: 305px;
    background: var(--ink); color: var(--white); padding: 50px 57px 0;
  }
  .law-title { font-weight: 700; font-size: 22px; margin-bottom: 10px; }
  .law-cite { font-size: 17px; line-height: 1.3; margin-bottom: 10px; }
  .law-text { font-size: 17px; line-height: 1.3; margin-bottom: 22px; }

  .footer {
    position: absolute; left: 0; top: 985px; width: 857px; height: 215px;
    display: flex; align-items: center; justify-content: space-between; padding: 0 50px;
  }
  .partner { display: flex; flex-direction: column; align-items: center; width: 200px; text-align: center; }
  .partner-name { font-weight: 700; font-size: 17px; color: var(--ink); line-height: 1.25; }
  .partner-mark { width: 22px; height: 22px; border-radius: 50%; background: var(--ink); margin-bottom: 8px; }
  .partner-sub { font-size: 15px; color: var(--ink); margin-top: 6px; }
  .brand-name { font-weight: 700; font-size: 24px; color: var(--navy); }
  .brand-mark { width: 22px; height: 22px; border-radius: 50%; background: var(--red); margin-bottom: 8px; }
  .note { width: 330px; font-size: 14px; line-height: 1.35; color: var(--grey); text-align: center; }
</style>
</head>
<body>
<div class="poster">
  <section class="hero">
    <div class="figure-area" role="img" aria-label="Silhouette of a blind pedestrian walking with a white cane"></div>
    <svg class="stop-sign" width="130" height="130" viewBox="0 0 130 130" aria-label="Stop">
      <circle cx="65" cy="65" r="62" fill="var(--white)"/>
      <circle cx="65" cy="65" r="54" fill="var(--red)"/>
      <text x="65" y="80" text-anchor="middle" font-family="Oswald, sans-serif" font-weight="700" font-size="42" fill="var(--white)">STOP</text>
    </svg>
    <h1 class="headline">
      <span class="line">Are you</span>
      <span class="line">aware?</span>
      <span class="state-law">Indiana Law</span>
    </h1>
  </section>

  <section class="law-band">
    <h2 class="law-title">INDIANA WHITE CANE LAW</h2>
    <p class="law-cite">Ind. Code § 9-21-17-21 : Indiana Code - Section 9-21-17-21: Blind pedestrians; yield of right-of-way</p>
    <p class="law-text">A person who drives a vehicle shall yield the right-of-way to a blind pedestrian carrying a clearly visible white cane or accompanied by a guide dog.</p>
    <h2 class="law-title">PENALTY</h2>
    <p class="law-cite">Ind. Code § 9-21-17-24 : Indiana Code - Section 9-21-17-24: Violations; Class C infraction</p>
    <p class="law-text">A person who violates this chapter commits a Class C infraction. (Misdemeanor)</p>
  </section>

  <footer class="footer">
    <div class="partner">
      <span class="partner-mark"></span>
      <span class="partner-name">Cedarbrook Society of Staff for Low Sight</span>
      <span class="partner-sub">Maple Ridge Chapter</span>
    </div>
    <p class="note">Lorem ipsum dolor sit nulla pariatur. Excepteur sint occaecat cupidatat, tempor incidunt ut labore et dolore magnam aliquam quaerat voluptatem.</p>
    <div class="partner">
      <span class="brand-mark"></span>
      <span class="brand-name">Bright Harbor</span>
    </div>
  </footer>
</div>
</body>
</html>
```